3 Medical Provider Brochures targeted at doctors and patients

We are a diagnostic imaging provider.

We need 3 brochure layouts.

1) A 4-fold with our 4 locations...one on each panel
2) A single-sheet brochure marketing each of our procedures to the referring physicians. (a shell, one completed so we clone the rest)
3) A single-sheet brochure handout containing information about certain exams and ways to prepare for our patients' education. (a shell, one completed so we can clone the rest)

Target Market(s)

4-fold target is for the referral coordinator in a doctors office, so they can find our location at-a-glance
One of the single broadsheets to the referring physician marketing a particular modality (CAT Scan, MRI, X-ray, Ultrasound, Mammography, Breast Biopsy)
The other single Broadsheet is marketed to patients but handed out by doctors who want to send patients to be scanned at our facility.

Industry/Entity Type

Medical Imaging

Font styles to use
Sans Serif

Colors
3276b5
0255a3
85cae6
ffffff

Requirements
Must have
• The 4-fold should be easy to read at-a-glance but contain some branding.
• The doctor-facing broadsheet should be in a the form of a shell, so we can do one for each of our modalities
• The patient-facing should be a shell as well, so we can do one for each of our major exams.
• Our name is KEL MRI and Imaging Centers. KEL means Keen Every Look. KEL IS Keen Every Look.
Nice to have
• Friendly faces, but professional and knowledgeable.
• Easy-to-update brochure shell contents

```html
<!DOCTYPE html>
<html lang="en">
<head>
<meta charset="utf-8">
<title>KEL MRI and Imaging Centers – Locations Brochure</title>
<link rel="stylesheet" href="https://fonts.googleapis.com/css2?family=Oswald:wght@500;600&family=Lato:wght@400&family=Roboto+Condensed:wght@300;400&display=swap">
<style>
  :root{
    --blue:#3276b5;
    --navy:#0255a3;
    --sky:#85cae6;
    --white:#ffffff;
    --deep:#1f63ad;
    --ink:#1d1d1d;
    --text:#2b2b2b;
    --rule:#3a3a3a;
    --page:#ececec;
  }
  html,body{margin:0;padding:0;overflow:hidden}
  body{width:1200px;height:1200px;background:var(--page);position:relative}
  .brochure{position:absolute;left:20px;top:249px;width:1160px;height:702px;display:flex;flex-wrap:wrap;box-shadow:0 2px 10px rgba(0,0,0,.18)}
  .panel{position:relative;width:290px;height:689px;overflow:hidden;font-family:"Lato",sans-serif}
  .panel--light{background:linear-gradient(90deg,#ffffff 0%,#f1f1f1 100%);color:var(--text)}
  .panel--blue{background:linear-gradient(180deg,#4f9be0 0%,#3a84cb 45%,#2a6fb8 100%);color:var(--white)}
  .panel--deep{background:linear-gradient(160deg,#2f74bd 0%,#1f63ad 60%,#1b5ba3 100%);color:var(--white)}
  .base-band{width:1160px;height:13px;background:var(--navy)}

  .item{position:absolute;left:0;right:0;text-align:center;transform:translateY(-50%);margin:0}
  .rule{position:absolute;height:2px;left:50%;transform:translateX(-50%)}
  .panel--light .rule{background:var(--rule)}
  .panel--blue .rule,.panel--deep .rule{background:rgba(255,255,255,.85)}

  .address{font-size:20px;line-height:33px}
  .phones{font-size:19px;line-height:22px}
  .phones span{display:inline-flex;align-items:center;gap:10px}
  .phones svg{width:16px;height:14px}
  .services{font-family:"Roboto Condensed",sans-serif;font-size:15.5px;line-height:21px;font-weight:400;padding:0 16px}
  .label{font-family:"Roboto Condensed",sans-serif;font-weight:300;font-size:16px;line-height:20px}
  .label--lato{font-family:"Lato",sans-serif;font-weight:400;font-size:16.5px}
  .person{font-family:"Oswald",sans-serif;font-weight:500;font-size:19px;line-height:22px;text-transform:uppercase;color:var(--ink)}
  .person--navy{color:#0c2f5c}
  .direct{font-size:14px;line-height:16px}
  .direct svg{width:9px;height:11px;vertical-align:-1px;margin-right:3px}

  .badge-circle{position:absolute;width:266px;height:266px;border-radius:50%;left:12px;top:-142px;box-sizing:border-box}
  .badge-circle--blue{background:var(--deep);border:4px solid var(--white);box-shadow:0 0 0 1px #d8d8d8}
  .badge-circle--white{background:var(--white);border:4px solid #7fb3e2}
  .badge-title{position:absolute;left:0;right:0;text-align:center;font-family:"Oswald",sans-serif;font-weight:500;font-size:26px;line-height:36px;text-transform:uppercase;transform:translateY(-50%)}
  .badge-title--sky{color:var(--sky)}
  .badge-title--navy{color:var(--navy)}

  .tab{position:absolute;left:14px;width:260px;border-radius:12px;display:flex;align-items:center;justify-content:center;text-align:center;font-family:"Oswald",sans-serif;font-weight:500;text-transform:uppercase}
  .tab--white{background:var(--white);color:var(--deep);top:549px;height:133px;font-size:27px;line-height:38px}
  .tab--blue{background:var(--deep);color:var(--sky);top:583px;height:98px;font-size:26px;line-height:28px;width:258px}
  .tab--brand{background:var(--white);top:582px;height:99px;width:259px}
  .brand-name{font-family:"Lato",sans-serif;font-weight:400;color:var(--navy);font-size:19px;line-height:24px;text-align:center}

  .waves{position:absolute;inset:0;width:290px;height:689px}
</style>
</head>
<body>
<svg width="0" height="0" style="position:absolute" aria-hidden="true">
  <symbol id="icon-phone" viewBox="0 0 16 14">
    <rect x="0" y="1" width="4" height="12" rx="1" fill="currentColor"/>
    <rect x="5" y="1" width="11" height="12" rx="1" fill="currentColor"/>
    <rect x="7" y="3" width="7" height="2" fill="#fff" opacity=".7"/>
    <rect x="7" y="7" width="2" height="2" fill="#fff" opacity=".7"/>
    <rect x="10" y="7" width="2" height="2" fill="#fff" opacity=".7"/>
    <rect x="7" y="10" width="2" height="2" fill="#fff" opacity=".7"/>
    <rect x="10" y="10" width="2" height="2" fill="#fff" opacity=".7"/>
  </symbol>
  <symbol id="icon-fax" viewBox="0 0 16 14">
    <path d="M1 3 Q8 -1 15 3 L15 5 L11 5 L11 4 L5 4 L5 5 L1 5 Z" fill="currentColor"/>
    <rect x="2" y="6" width="12" height="7" rx="1.5" fill="currentColor"/>
    <circle cx="8" cy="9.5" r="1.8" fill="#fff" opacity=".7"/>
  </symbol>
  <symbol id="icon-handset" viewBox="0 0 9 11">
    <path d="M2 0 L4 2.5 L3 4 Q3.5 6.5 5.5 8 L7 7 L9 9.5 L7.5 11 Q1 9 0 1.5 Z" fill="currentColor"/>
  </symbol>
</svg>

<main class="brochure">
  <!-- Plantation -->
  <section class="panel panel--light">
    <div class="badge-circle badge-circle--blue"></div>
    <p class="badge-title badge-title--sky" style="top:50px">Plantation<br>Location</p>
    <p class="item address" style="top:209px">5120 West Palm Breeze Blvd.<br>Plantation, Florida 33300</p>
    <div class="rule" style="top:266px;width:214px"></div>
    <p class="item phones" style="top:311px"><span><svg><use href="#icon-phone"/></svg>954.555.0141</span><br><span><svg><use href="#icon-fax"/></svg>954.555.0172</span></p>
    <div class="rule" style="top:350px;width:188px"></div>
    <p class="item services" style="top:404px;text-align:justify;text-align-last:center">Provides High-field MRI, Open MRI, Helical CT, Ultrasound, X-ray, DEXA, Breast Biopsy and Mammography</p>
    <p class="item label" style="top:466px">Your Marketing Associates are</p>
    <p class="item person" style="top:494px">Lorena Castillo</p>
    <p class="item direct" style="top:517px"><svg><use href="#icon-handset"/></svg>555-555-5555</p>
    <p class="item person" style="top:541px">Eva Moreno</p>
    <p class="item direct" style="top:564px"><svg><use href="#icon-handset"/></svg>555-555-5555</p>
    <div class="rule" style="top:584px;width:186px;height:1px"></div>
    <p class="item label label--lato" style="top:601px">Your Facility Manager is</p>
    <p class="item person" style="top:628px">Grace Dumont</p>
    <p class="item direct" style="top:651px"><svg><use href="#icon-handset"/></svg>555-555-5555</p>
    <div class="rule" style="top:668px;width:186px;height:1px"></div>
  </section>

  <!-- Coral Springs / Margate -->
  <section class="panel panel--blue">
    <p class="item address" style="top:128px;line-height:24px;padding:0 14px">1900 N. Harbor Road, Suite 210<br>Margate FL 33000</p>
    <div class="rule" style="top:233px;width:232px"></div>
    <p class="item phones" style="top:272px"><span><svg><use href="#icon-phone"/></svg>954-555-0110</span><br><span><svg><use href="#icon-fax"/></svg>954-555-0172</span></p>
    <div class="rule" style="top:316px;width:232px"></div>
    <p class="item label" style="top:367px;font-size:17px;color:#e4f3fb">Provides Ultra High Field 3.0T MRI</p>
    <p class="item label" style="top:406px;font-size:17px;color:#e4f3fb">Your Marketing Associate is</p>
    <p class="item person person--navy" style="top:439px;font-size:20px">Paula Brenner</p>
    <p class="item direct" style="top:465px"><svg><use href="#icon-handset"/></svg>555-555-5555</p>
    <div class="tab tab--white">Coral<br>Springs/Margate<br>Location</div>
  </section>

  <!-- Cooper City -->
  <section class="panel panel--light">
    <p class="item address" style="top:100px">12040 Orchid Street,<br>Suite 205<br>Cooper City, FL 33020</p>
    <div class="rule" style="top:160px;width:215px"></div>
    <p class="item phones" style="top:196px"><span><svg><use href="#icon-phone"/></svg>954.555.0188</span><br><span><svg><use href="#icon-fax"/></svg>954.555.0193</span></p>
    <div class="rule" style="top:233px;width:215px"></div>
    <p class="item services" style="top:303px;padding:0 6px;color:var(--ink)">Provides High-field MRI, Helical CT, Ultrasound, X-ray, DEXA, Breast Biopsy and Mammography</p>
    <p class="item label" style="top:353px">Your Marketing Associates are</p>
    <p class="item person" style="top:382px">Sofia Rendon</p>
    <p class="item direct" style="top:405px"><svg><use href="#icon-handset"/></svg>555-555-5555</p>
    <p class="item person" style="top:429px">Mark Dalton</p>
    <p class="item direct" style="top:452px"><svg><use href="#icon-handset"/></svg>555-555-5555</p>
    <div class="rule" style="top:471px;width:186px;height:1px"></div>
    <p class="item label label--lato" style="top:489px">Your Facility Manager is</p>
    <p class="item person" style="top:516px">Laura Whitley</p>
    <p class="item direct" style="top:539px"><svg><use href="#icon-handset"/></svg>954-555-0188</p>
    <div class="rule" style="top:555px;width:186px;height:1px"></div>
    <div class="tab tab--blue">Cooper City<br>Location</div>
  </section>

  <!-- Boca -->
  <section class="panel panel--deep">
    <svg class="waves" viewBox="0 0 290 689" aria-hidden="true">
      <path d="M0 420 Q150 360 290 200" fill="none" stroke="#ffffff" stroke-opacity=".06" stroke-width="60"/>
      <path d="M0 560 Q170 500 290 340" fill="none" stroke="#ffffff" stroke-opacity=".05" stroke-width="40"/>
    </svg>
    <div class="badge-circle badge-circle--white" style="top:-146px"></div>
    <p class="badge-title badge-title--navy" style="top:53px">Boca<br>Location</p>
    <p class="item address" style="top:193px">3400 North Coral Trail<br>Suite 140<br>Boca Raton, FL 33430</p>
    <p class="item services" style="top:284px;color:#d7ecf8">Provides High-field MRI, Ultrasound, X-ray and Mammography</p>
    <p class="item label" style="top:338px;color:#d7ecf8">Your Marketing Associate is</p>
    <p class="item person person--navy" style="top:362px">Diego Salas</p>
    <p class="item direct" style="top:385px"><svg><use href="#icon-handset"/></svg>555-555-5555</p>
    <div class="rule" style="top:396px;width:186px;height:1px"></div>
    <p class="item label label--lato" style="top:412px;color:#d7ecf8">Your Facility Manager is</p>
    <p class="item person person--navy" style="top:436px">Jill Harmon</p>
    <p class="item direct" style="top:461px"><svg><use href="#icon-handset"/></svg>561-555-0126</p>
    <div class="rule" style="top:480px;width:186px;height:1px"></div>
    <p class="item phones" style="top:529px"><span><svg><use href="#icon-phone"/></svg>561.555.0126</span><br><span><svg><use href="#icon-fax"/></svg>561.555.0167</span></p>
    <div class="tab tab--brand">
      <p class="brand-name">KEL MRI and<br>Imaging Centers</p>
    </div>
  </section>

  <div class="base-band"></div>
</main>
</body>
</html>
```